Cloud Based Bookkeeping Website for Florists (Flower Shops)

We need a single page responsive website for a bookkeeping firm specializing in the floral industry. Our business model is based on the cloud and a goal is to attain floral clients from around the country, not only local.

Currently, we are attracted to flat illustration designs, but are concerned that they appear to informal or unprofessional. This webdesign should communicate professionalism, yet approachable, bright, attractive and modern.

The color scheme and overall design should match our designed logo, which is attached, and icon sets. We are open to new icon ideas and layout design, other than the layout we prepared and attached.

The attached layout we prepared has a holding place for a video at the top section. We own the video and can provide at a later time to insert. There is another secondary holding place for an explanation video, which we may or may not need, depending on the design your submit.

Lastly, I want to reiterate that we are open to new layout ideas.

Target Market(s)

Florists, Flower Shops

Industry/Entity Type

Bookkeeper

Number of Pages Required

2 page

Font styles to use
Sans Serif

Requirements
Must have
• Each section should be full width and screen height.
• Full page/section scrolling
• A price table
• A scrolling or fixed section displaying the third party app we work with.
• A blog page and a scrolling carousel displaying recent blog posts.
• Services section should be the six listed, but expandable to add more.
• A lead generation page, where clients can add attachments
• Must be a WordPress design so owner can easily modify and edit in the future
• Must be able to accommodate java script snippets in the header.
Nice to have
• A fixed "Contact Us" tab on the right side of the page that will lead to a contact form.

```html
<!DOCTYPE html>
<html lang="en">
<head>
<meta charset="utf-8">
<title>PetalBooks — Cloud Bookkeeping for Florists</title>
<link href="https://fonts.googleapis.com/css2?family=Oswald:wght@400;500;600&family=Open+Sans:wght@400;600;700&display=swap" rel="stylesheet">
<style>
:root{
  --orange:#f15a24;
  --orange-dark:#d9481a;
  --teal:#26a6c1;
  --ink:#333333;
  --muted:#666666;
  --dark:#2e2e2e;
  --darker:#222222;
  --light:#f4f4f4;
  --line:#dddddd;
  --white:#ffffff;
}
*{box-sizing:border-box;margin:0;padding:0}
html,body{width:1200px;height:5310px;overflow:hidden}
body{font-family:"Open Sans",Arial,sans-serif;color:var(--ink);background:var(--white);font-size:15px;line-height:1.6}
.section{position:relative;width:1200px;overflow:hidden}
.heading{font-family:"Oswald",Arial,sans-serif;font-weight:500;font-size:42px;letter-spacing:1px;text-transform:uppercase;text-align:center;line-height:1.2}
.heading .o{color:var(--orange)}
.heading .t{color:var(--teal)}
.divider{display:block;margin:10px auto 0;width:30px;height:30px}
.btn{display:inline-block;font-family:"Oswald",Arial,sans-serif;font-size:15px;letter-spacing:.5px;text-transform:uppercase;padding:8px 22px;border-radius:22px;border:2px solid var(--orange);color:var(--orange);background:transparent}
.btn.fill{background:var(--orange);color:var(--white)}
.btn.white{background:var(--white);color:var(--orange);border-color:var(--white)}
.btn.teal{background:var(--teal);border-color:var(--teal);color:var(--white)}
.photo{position:absolute}

/* hero */
.hero{height:549px}
.hero .photo{inset:0;background:linear-gradient(160deg,#3b2a22 0%,#6a3c2c 30%,#8a5a3a 55%,#5d2f35 75%,#2e2420 100%)}
.hero .shade{position:absolute;inset:0;background:rgba(20,20,20,.35)}
.nav{position:absolute;top:0;left:0;right:0;height:100px;display:flex;align-items:center;padding:0 70px 30px}
.brand{display:flex;align-items:center;gap:10px;font-family:"Oswald",Arial,sans-serif;font-size:30px;font-weight:500;color:var(--white)}
.brand .mark{width:30px;height:30px;background:var(--orange);border-radius:4px}
.menu{margin-left:auto;display:flex;gap:30px;align-items:center;list-style:none;font-family:"Oswald",Arial,sans-serif;font-size:15px;color:var(--white);text-transform:uppercase}
.menu .active{color:var(--orange)}
.play{position:absolute;left:0;right:0;top:240px;text-align:center;color:var(--white);font-family:"Oswald",Arial,sans-serif;font-size:22px;letter-spacing:1px}
.play svg{display:block;margin:0 auto 8px}

/* why */
.why{height:460px;padding-top:45px}
.why p{width:1010px;margin:20px auto 0;text-align:center;font-size:15px;color:var(--ink)}
.why p + p{margin-top:10px}
.actions{margin-top:26px;text-align:center;display:flex;justify-content:center;gap:14px}

/* how */
.how{height:521px;background:var(--light);padding-top:45px}
.how .video{left:99px;top:150px;width:591px;height:337px;background:linear-gradient(135deg,#d8d6d2 0%,#b9b6b1 50%,#8b8884 100%)}
.how .video svg{position:absolute;left:50%;top:50%;transform:translate(-50%,-50%)}
.how .copy{position:absolute;left:725px;top:145px;width:395px;font-size:14.5px}
.how .copy strong{color:var(--teal)}
.how .actions{justify-content:flex-start;margin-top:16px}

/* services */
.services{height:636px;padding-top:40px}
.services .photo{inset:0;background:linear-gradient(180deg,#f47a44 0%,#f26a30 50%,#ef6226 100%)}
.services .heading{color:var(--white);position:relative}
.services .divider{position:relative}
.grid{position:relative;width:1030px;margin:38px auto 0;display:grid;grid-template-columns:repeat(3,1fr);column-gap:40px;row-gap:40px}
.service{display:flex;gap:16px;color:var(--white);border-bottom:1px solid rgba(255,255,255,.35);padding-bottom:22px}
.service .ico{flex:0 0 62px;height:62px;border-radius:50%;background:var(--white);display:flex;align-items:center;justify-content:center}
.service h3{font-family:"Oswald",Arial,sans-serif;font-weight:500;font-size:17px;text-transform:uppercase}
.service p{font-size:13px;line-height:1.5}
.services .more{position:relative;text-align:center;margin-top:34px}

/* outsourced */
.outsourced{height:454px;padding-top:36px}
.outsourced .body{width:900px;margin:20px auto 0;text-align:center;font-size:14px;line-height:1.5}
.outsourced .body p{margin-bottom:8px}
.outsourced .body b{font-weight:700}

/* cost */
.cost{height:425px;background:var(--light);padding-top:34px}
.cost .body{width:900px;margin:22px auto 0;text-align:center;font-size:14px;line-height:1.55}
.cost .body p{margin-bottom:8px}
.perks{display:grid;grid-template-columns:1fr 1fr;width:620px;margin:8px auto 16px;text-align:left;list-style:none;row-gap:6px;font-size:14px}
.perks li::before{content:"";display:inline-block;width:8px;height:8px;border-radius:50%;background:var(--orange);margin-right:10px;vertical-align:middle}

/* pricing */
.pricing{height:815px;padding-top:44px}
.plans{position:absolute;top:140px;left:134px;width:935px;height:650px}
.plan{position:absolute;background:var(--dark);color:var(--white);text-align:center;border-radius:8px;font-family:"Oswald",Arial,sans-serif}
.plan.left{left:0;top:34px;width:291px;height:570px}
.plan.right{left:645px;top:34px;width:291px;height:570px}
.plan.mid{left:298px;top:0;width:340px;height:640px;background:var(--orange);box-shadow:0 6px 20px rgba(0,0,0,.25)}
.plan h3{font-weight:500;font-size:26px;line-height:1.15;margin-top:40px;text-transform:uppercase}
.plan .price{font-size:58px;font-weight:400;margin-top:12px;line-height:1}
.plan .price sup{font-size:24px;vertical-align:top}
.plan .price small{font-size:13px}
.plan ul{list-style:none;margin:22px 34px 0;font-family:"Open Sans",Arial,sans-serif;font-size:14.5px;font-weight:600}
.plan li{padding:12px 0;border-bottom:1px solid rgba(255,255,255,.25)}
.plan .btn{margin-top:30px;background:var(--white);color:var(--ink);border-color:var(--white)}

/* convince */
.convince{height:565px;background:var(--light);padding-top:40px}
.convince .lede{width:800px;margin:22px auto 0;text-align:center;font-size:14px;line-height:1.5}
.form{position:absolute;left:99px;top:245px;width:627px;display:grid;grid-template-columns:1fr 1fr;column-gap:24px;row-gap:16px}
.field label{display:block;font-size:12.5px;margin-bottom:4px}
.field span{display:block;height:42px;background:var(--white);border:1px solid var(--line);padding:10px 12px;font-size:12.5px;color:#aaa}
.submit{grid-column:2;height:44px;background:var(--orange);color:var(--white);font-family:"Oswald",Arial,sans-serif;font-size:17px;text-transform:uppercase;display:flex;align-items:center;justify-content:center;align-self:end}
.drop{position:absolute;left:754px;top:262px;width:350px;height:250px;background:#e2e2e2;display:flex;align-items:center;justify-content:center;font-family:"Oswald",Arial,sans-serif;font-size:17px;text-transform:uppercase;color:var(--ink)}

/* blog */
.blog{height:460px;padding-top:36px}
.posts{position:absolute;left:99px;top:140px;width:1006px;display:grid;grid-template-columns:repeat(4,1fr);column-gap:20px}
.post .img{position:relative;height:200px}
.post .date{position:absolute;left:0;top:0;width:56px;background:var(--orange);color:var(--white);text-align:center;font-family:"Oswald",Arial,sans-serif;font-size:24px;line-height:1.1;padding:6px 0}
.post .date small{display:block;font-size:12px}
.post h4{font-size:14px;font-weight:700;margin-top:10px;line-height:1.3}
.post p{font-size:12px;color:var(--muted);line-height:1.45;margin-top:4px}
.p1{background:linear-gradient(135deg,#8ea25a,#c9a36b 60%,#5c6e34)}
.p2{background:linear-gradient(135deg,#7f8a3a,#c24a3a 55%,#6d7a30)}
.p3{background:linear-gradient(135deg,#b84b55,#e0a346 50%,#8d3a3f)}
.p4{background:linear-gradient(135deg,#f0b030,#e88a20 50%,#c26a18)}

/* partners */
.partners{height:105px;background:#eeeeee;display:flex;align-items:center}
.partners .tag{width:250px;height:105px;background:var(--orange);color:var(--white);font-family:"Oswald",Arial,sans-serif;font-size:24px;line-height:1.15;padding:24px 0 0 90px;text-transform:uppercase;clip-path:polygon(0 0,100% 0,86% 100%,0 100%)}
.partners .arrow{width:40px;text-align:center;color:#999;font-size:26px}
.logos{flex:1;display:flex;justify-content:space-around;align-items:center;font-family:"Open Sans",Arial,sans-serif;font-weight:700;font-size:24px;color:#555}
.logos span{display:flex;align-items:center;gap:10px}
.logos i{display:inline-block;width:20px;height:20px;border-radius:50%;background:#777}

/* footer */
.footer{height:285px;background:var(--darker);color:#cccccc}
.footer .col{position:absolute;top:40px;font-size:13px}
.footer h5{font-family:"Oswald",Arial,sans-serif;font-weight:500;font-size:18px;color:var(--white);text-transform:uppercase;margin-bottom:14px}
.contact{left:99px;width:330px}
.contact li{list-style:none;display:flex;gap:10px;align-items:flex-start;margin-bottom:8px}
.contact svg{flex:0 0 14px;margin-top:3px}
.news{left:470px;width:330px}
.news .input{height:36px;background:var(--white);margin:14px 0 10px;width:300px}
.news .btn{border-radius:0;padding:4px 14px;font-size:13px}
.footer .corner{position:absolute;right:0;top:0;width:340px;height:285px;background:var(--orange);clip-path:polygon(22% 0,100% 0,100% 100%,0 100%)}
.footer .corner .brand{position:absolute;left:110px;top:95px;font-size:30px}
.social{position:absolute;left:140px;top:150px;display:flex;gap:10px}
.social i{width:26px;height:26px;border-radius:50%;background:var(--white);display:block}
.copyright{height:35px;background:#161616;color:#bbbbbb;font-size:12px;text-align:center;line-height:35px}
</style>
</head>
<body>

<header class="section hero">
  <div class="photo" role="img" aria-label="Photograph of a flower shop interior with colourful bouquets on display"></div>
  <div class="shade"></div>
  <nav class="nav">
    <div class="brand"><span class="mark"></span>PetalBooks</div>
    <ul class="menu">
      <li class="active">Home</li><li>Why PetalBooks</li><li>What We Do</li><li>Pricing</li><li>Clients</li><li>Blog</li>
      <li><span class="btn fill">Contact Us</span></li>
    </ul>
  </nav>
  <div class="play">
    <svg width="84" height="84" viewBox="0 0 84 84"><circle cx="42" cy="42" r="40" fill="#ffffff"/><circle cx="42" cy="42" r="31" fill="none" stroke="#f15a24" stroke-width="3"/><path d="M35 28 L58 42 L35 56 Z" fill="#f15a24"/></svg>
    PLAY VIDEO
  </div>
</header>

<section class="section why">
  <h2 class="heading">Why <span class="o">PetalBooks</span></h2>
  <svg class="divider" viewBox="0 0 30 30"><circle cx="15" cy="15" r="6" fill="none" stroke="#999" stroke-width="2"/><line x1="0" y1="15" x2="8" y2="15" stroke="#999"/><line x1="22" y1="15" x2="30" y2="15" stroke="#999"/></svg>
  <p>We'll be real: You chose a path of a sole-proprietor and self-employment to make money, not waste it spending time sifting through receipts, processing invoices to pay your vendors, and preparing statements for your tax preparer. Your time can be better spent growing your business, not bookkeeping for your business.</p>
  <p>Although we can proudly call ourselves designers, we've been in the floral industry for many years - washing buckets, cutting boxes, stocking shelves, delivering flowers, not to mention the sleepless holidays. Bookkeeping for a family flower shop started as a hobby, but transformed into an obsession. We understand the hard work and dedication that it takes to operate a successful flower shop and the profitability metrics every shop should strive to meet. Let us manage the stress of bookkeeping so you can focus on customer satisfaction and business growth!</p>
  <div class="actions"><span class="btn fill">Sign Up</span><span class="btn">Get Your Quote</span></div>
</section>

<section class="section how">
  <h2 class="heading"><span class="o">Here's</span> <span class="t">How It Works</span></h2>
  <svg class="divider" viewBox="0 0 30 30"><circle cx="15" cy="15" r="6" fill="none" stroke="#999" stroke-width="2"/><line x1="0" y1="15" x2="8" y2="15" stroke="#999"/><line x1="22" y1="15" x2="30" y2="15" stroke="#999"/></svg>
  <div class="photo video" role="img" aria-label="Explainer video still of a person working at a laptop">
    <svg width="70" height="70" viewBox="0 0 70 70"><circle cx="35" cy="35" r="33" fill="rgba(255,255,255,.85)"/><path d="M29 22 L49 35 L29 48 Z" fill="#555"/></svg>
  </div>
  <div class="copy">
    <p><strong>We tried hard to make this really simple!</strong><br>After joining our team, we'll send you a scanner and set it up for you. You simply scan your receipts, bills, &amp; invoices to us and we'll send you financial statements at the intervals you need them. Although we won't be printing and sending your bill payments, we'll send them to our payment processor where you'll log in and approve each bill – keeping you in full control of your bank account.<br>Any opportunity we see to save you money, we'll reach out and let you know.<br>It really is that simple!</p>
    <div class="actions"><span class="btn teal">Sign Up</span><span class="btn">Get Your Quote</span></div>
  </div>
</section>

<section class="section services">
  <div class="photo" role="img" aria-label="Orange-tinted photograph of a busy office with people at work"></div>
  <h2 class="heading">What We Do</h2>
  <svg class="divider" viewBox="0 0 30 30"><circle cx="15" cy="15" r="6" fill="none" stroke="#fff" stroke-width="2"/><line x1="0" y1="15" x2="8" y2="15" stroke="#fff"/><line x1="22" y1="15" x2="30" y2="15" stroke="#fff"/></svg>
  <div class="grid">
    <div class="service"><div class="ico"><svg width="30" height="30" viewBox="0 0 30 30"><rect x="7" y="4" width="16" height="22" fill="none" stroke="#f15a24" stroke-width="2"/><line x1="10" y1="10" x2="20" y2="10" stroke="#f15a24" stroke-width="2"/><line x1="10" y1="15" x2="20" y2="15" stroke="#f15a24" stroke-width="2"/><line x1="10" y1="20" x2="17" y2="20" stroke="#f15a24" stroke-width="2"/></svg></div><div><h3>Bookkeeping</h3><p>If you send us a receipt, it'll be attached to its transaction for easy reference. Books are kept up to date each week.</p></div></div>
    <div class="service"><div class="ico"><svg width="30" height="30" viewBox="0 0 30 30"><circle cx="15" cy="15" r="11" fill="none" stroke="#f15a24" stroke-width="2"/><text x="15" y="20" text-anchor="middle" font-size="14" font-family="Arial" fill="#f15a24">$</text></svg></div><div><h3>Payroll</h3><p>Employees are paid on time with taxes filed and forms prepared, so you never miss a deadline.</p></div></div>
    <div class="service"><div class="ico"><svg width="30" height="30" viewBox="0 0 30 30"><path d="M5 15 L15 5 L25 5 L25 15 L15 25 Z" fill="none" stroke="#f15a24" stroke-width="2"/><circle cx="20" cy="10" r="2" fill="#f15a24"/></svg></div><div><h3>Sales Tax</h3><p>Your sales tax is filed every period and paid on time, so the state never comes knocking.</p></div></div>
    <div class="service"><div class="ico"><svg width="30" height="30" viewBox="0 0 30 30"><rect x="6" y="17" width="4" height="8" fill="#f15a24"/><rect x="13" y="11" width="4" height="14" fill="#f15a24"/><rect x="20" y="6" width="4" height="19" fill="#f15a24"/></svg></div><div><h3>Financial Statements</h3><p>Statements delivered on your schedule give a clear view of how the shop is really doing.</p></div></div>
    <div class="service"><div class="ico"><svg width="30" height="30" viewBox="0 0 30 30"><rect x="4" y="8" width="22" height="15" rx="2" fill="none" stroke="#f15a24" stroke-width="2"/><line x1="4" y1="13" x2="26" y2="13" stroke="#f15a24" stroke-width="2"/></svg></div><div><h3>Accounts Payable</h3><p>Send us your bills and invoices; we prepare payments for your quick approval each week.</p></div></div>
    <div class="service"><div class="ico"><svg width="30" height="30" viewBox="0 0 30 30"><path d="M8 12 A8 8 0 0 1 22 10" fill="none" stroke="#f15a24" stroke-width="2"/><path d="M22 18 A8 8 0 0 1 8 20" fill="none" stroke="#f15a24" stroke-width="2"/><path d="M22 5 L22 10 L17 10" fill="none" stroke="#f15a24" stroke-width="2"/><path d="M8 25 L8 20 L13 20" fill="none" stroke="#f15a24" stroke-width="2"/></svg></div><div><h3>Reconciliations</h3><p>Every account is matched to its bank statement monthly, so nothing slips through the cracks.</p></div></div>
  </div>
  <div class="more"><span class="btn white">More Services</span></div>
</section>

<section class="section outsourced">
  <h2 class="heading"><span class="o">Outsourced</span> <span class="t">Bookkeeping? Whoa!</span></h2>
  <svg class="divider" viewBox="0 0 30 30"><circle cx="15" cy="15" r="6" fill="none" stroke="#999" stroke-width="2"/><line x1="0" y1="15" x2="8" y2="15" stroke="#999"/><line x1="22" y1="15" x2="30" y2="15" stroke="#999"/></svg>
  <div class="body">
    <p><b>Yeah, thanks to the cloud – it's a thing!</b><br>In-house bookkeeping can become expensive – and although that bookkeeper sitting in your office doesn't seem to bother too much, there are costs associated with that space, equipment and software they are using. Think of the things you can do with that space, perhaps there is a need to expand your work space or it's a perfect location for a new floral designer that can generate income, not an expense!</p>
    <p>Let's not even talk about employing a full-time bookkeeper!</p>
    <p>According to national wage data, the median annual wage for a bookkeeper was $38,390 in May 2016. Unless your shop's annual revenue is well above $2 million dollars, employing a full-time bookkeeper is not cost effective. This doesn't even factor any other associated costs related to industry specific training.</p>
    <p>An outsourced bookkeeper can work in their own space and use their own equipment, thus saving you time and money (isn't this the goal?)</p>
  </div>
</section>

<section class="section cost">
  <h2 class="heading"><span class="o">So, What Does</span> <span class="t">It Cost You Say?</span></h2>
  <svg class="divider" viewBox="0 0 30 30"><circle cx="15" cy="15" r="6" fill="none" stroke="#999" stroke-width="2"/><line x1="0" y1="15" x2="8" y2="15" stroke="#999"/><line x1="22" y1="15" x2="30" y2="15" stroke="#999"/></svg>
  <div class="body">
    <p><b>Slow down! We'll get there.  First let's talk about what you get and how save with PetalBooks.</b><br>We want you to rest assured that our costs to you will remain fixed for the term of our agreement and for only the services you need.  That's right, no surprise fees or added billable hours!  You pay for only the services you need.</p>
    <p><b>Once you become our client, you'll get a:</b></p>
    <ul class="perks">
      <li>A PaperPilot Document Scanner</li><li>Payroll Subscription</li>
      <li>Accounting Software Subscription</li><li>Accounts Payable Subscription</li>
    </ul>
    <p><b>Alright, alright!  Now that you know what you won't have to pay, it's time to customize your quote and close the deal!</b></p>
  </div>
</section>

<section class="section pricing">
  <h2 class="heading"><span class="o">Pricing</span></h2>
  <svg class="divider" viewBox="0 0 30 30"><circle cx="15" cy="15" r="6" fill="none" stroke="#999" stroke-width="2"/><line x1="0" y1="15" x2="8" y2="15" stroke="#999"/><line x1="22" y1="15" x2="30" y2="15" stroke="#999"/></svg>
  <div class="plans">
    <div class="plan left"><h3>Monthly<br>Plan</h3><div class="price"><sup>$</sup>25<small>/mo</small></div><ul><li>Lorem Ipsum Dolor</li><li>Sit Amet, Consectetuer</li><li>Adipiscing Elit</li><li>Sed Diam Nonummy Nibh</li></ul><span class="btn">Get Started</span></div>
    <div class="plan mid"><h3>Yearly<br>Plan</h3><div class="price"><sup>$</sup>200<small>/yr</small></div><ul><li>Lorem Ipsum Dolor</li><li>Sit Amet, Consectetuer</li><li>Adipiscing Elit</li><li>Sed Diam Nonummy Nibh</li><li>Lorem Ipsum Dolor</li></ul><span class="btn">Get Started</span></div>
    <div class="plan right"><h3>Lifetime Plan<br>(10 Years)</h3><div class="price"><sup>$</sup>1500</div><ul><li>Lorem Ipsum Dolor</li><li>Sit Amet, Consectetuer</li><li>Adipiscing Elit</li><li>Sed Diam Nonummy Nibh</li></ul><span class="btn">Get Started</span></div>
  </div>
</section>

<section class="section convince">
  <h2 class="heading"><span class="o">Still Not</span> <span class="t">Convinced?</span></h2>
  <svg class="divider" viewBox="0 0 30 30"><circle cx="15" cy="15" r="6" fill="none" stroke="#999" stroke-width="2"/><line x1="0" y1="15" x2="8" y2="15" stroke="#999"/><line x1="22" y1="15" x2="30" y2="15" stroke="#999"/></svg>
  <p class="lede"><b>Then we can only assume that you're not lying underneath a pile of receipts!</b><br>No worries, we can still be friends! – Let us create a free one-time service profitability report for you.<br>That's right FREE, this one is on us.</p>
  <div class="form">
    <div class="field"><label>Shop Name</label><span>Shop Name</span></div>
    <div class="field"><label>Website Address</label><span>Website Address</span></div>
    <div class="field"><label>Your Name</label><span>Your Name</span></div>
    <div class="field"><label>Telephone Number</label><span>Telephone Number</span></div>
    <div class="field"><label>E-mail</label><span>E-mail</span></div>
    <div class="submit">Submit</div>
  </div>
  <div class="drop">Drag and drop your statement here</div>
</section>

<section class="section blog">
  <h2 class="heading"><span class="o">Latest</span> <span class="t">Blog</span></h2>
  <svg class="divider" viewBox="0 0 30 30"><circle cx="15" cy="15" r="6" fill="none" stroke="#999" stroke-width="2"/><line x1="0" y1="15" x2="8" y2="15" stroke="#999"/><line x1="22" y1="15" x2="30" y2="15" stroke="#999"/></svg>
  <div class="posts">
    <article class="post"><div class="img p1" role="img" aria-label="Photo of a florist arranging flowers"><div class="date">28<small>MAY</small></div></div><h4>Sed ut perspiciatis unde omniste Lorem.</h4><p>Lorem ipsum dolor sit amet, consectetuer adipiscing elit, sed diam nonummy nibh euismod.</p></article>
    <article class="post"><div class="img p2" role="img" aria-label="Photo of potted plants on a shop table"><div class="date">28<small>MAY</small></div></div><h4>Sed ut perspiciatis unde omniste Lorem.</h4><p>Lorem ipsum dolor sit amet, consectetuer adipiscing elit, sed diam nonummy nibh euismod.</p></article>
    <article class="post"><div class="img p3" role="img" aria-label="Photo of a colourful flower bouquet"><div class="date">28<small>MAY</small></div></div><h4>Sed ut perspiciatis unde omniste Lorem.</h4><p>Lorem ipsum dolor sit amet, consectetuer adipiscing elit, sed diam nonummy nibh euismod.</p></article>
    <article class="post"><div class="img p4" role="img" aria-label="Photo of yellow and orange roses"><div class="date">28<small>MAY</small></div></div><h4>Sed ut perspiciatis unde omniste Lorem.</h4><p>Lorem ipsum dolor sit amet, consectetuer adipiscing elit, sed diam nonummy nibh euismod.</p></article>
  </div>
</section>

<section class="section partners">
  <div class="tag">Our<br>Partner</div>
  <div class="arrow">‹</div>
  <div class="logos"><span><i></i>Rosterly</span><span><i></i>LedgerPad</span><span><i></i>Docklet</span><span><i></i>PayNest</span></div>
  <div class="arrow">›</div>
</section>

<footer class="section footer">
  <div class="col contact">
    <h5>Contact Address</h5>
    <ul>
      <li><svg width="14" height="14" viewBox="0 0 14 14"><path d="M7 1a4 4 0 0 1 4 4c0 3-4 8-4 8S3 8 3 5a4 4 0 0 1 4-4z" fill="#fff"/></svg>Lorem ipsum dolor sit amet, consectetuer adipiscing elit, sed diam nonummy nibh euismod.</li>
      <li><svg width="14" height="14" viewBox="0 0 14 14"><path d="M3 1l3 3-1.5 2a8 8 0 0 0 3.5 3.5L10 8l3 3-2 2C6 13 1 8 1 3z" fill="#fff"/></svg>123-456-7890</li>
      <li><svg width="14" height="14" viewBox="0 0 14 14"><path d="M3 1l3 3-1.5 2a8 8 0 0 0 3.5 3.5L10 8l3 3-2 2C6 13 1 8 1 3z" fill="#fff"/></svg>123-456-7890</li>
      <li><svg width="14" height="14" viewBox="0 0 14 14"><rect x="1" y="3" width="12" height="8" fill="none" stroke="#fff"/><path d="M1 3l6 5 6-5" fill="none" stroke="#fff"/></svg>info@petalbooksbookkeeping.com</li>
    </ul>
  </div>
  <div class="col news">
    <h5>Newsletter Signup</h5>
    <p>Get The Latest Updates By Entering Your Email Address</p>
    <div class="input"></div>
    <span class="btn fill">Subscribe</span>
  </div>
  <div class="corner">
    <div class="brand"><span class="mark" style="background:#fff"></span>PetalBooks</div>
    <div class="social"><i></i><i></i><i></i></div>
  </div>
</footer>
<div class="copyright">Copyright © 2017 petalbooksbookkeeping.com, All Right Reserved.</div>

</body>
</html>
```